Design a menu for health restaurant

A health food restaurant in Los Angeles is seeking menu design. Our foods are made from scratch using whole ingredients.
Name: Grubb Larder
Address: 1000 E 60th StLos Angeles, CA 90247
Website: www.GrubbLarder.example
We are looking for a clean and simple menu. Brand colors are white/tan, green and orange.

Please see attached excel with menu items and logo. We do not yet have prices.

Colors
f78f20
9bcb3c
ffffff
fff3d1

Requirements
Must have
• Easy to read.
Trifold menu design (front and back).
VEGAN, VEGETARIAN, GLUTEN FREE, CONTAINS NUTS symbols.
Logo.
Nice to have
• Incorporate brand colors, but still be easy to read.
We would like to use the Belco font (attached) if it works. If not we are open to a similar font that is easy to read.

Please see attached images.
We like the images and headers of OPTION 1. Would like something similar in trifold format.
We like the clean fonts of OPTION 2.

```html
<!DOCTYPE html>
<html lang="en">
<head>
<meta charset="utf-8">
<title>Grubb Larder Menu</title>
<link rel="stylesheet" href="https://fonts.googleapis.com/css2?family=Rye&family=Ubuntu:wght@300;400;500&display=swap">
<style>
:root{
  --orange:#f78f20;
  --green:#9bcb3c;
  --white:#ffffff;
  --tan:#fff3d1;
  --paper:#fffaf3;
  --ink:#222222;
  --ink-soft:#444444;
  --dark:#2a2a2a;
  --stage:#e6e4df;
}
*{box-sizing:border-box;margin:0;padding:0}
html,body{width:1200px;height:1200px;overflow:hidden;background:var(--stage)}
.menu{position:absolute;left:20px;top:149px;width:1160px;height:902px;background:var(--paper);font-family:"Ubuntu",sans-serif;color:var(--ink)}
.panel{position:absolute;top:0;height:902px}
.panel--left{left:0;width:386px}
.panel--middle{left:388px;width:386px;background:var(--green)}
.panel--right{left:774px;width:386px}
.section{position:absolute;left:31px;width:340px;display:flex;flex-direction:column}
.panel--middle .section{left:23px}
.panel--right .section{left:17px}
.section-title{height:41px;flex:none;display:flex;align-items:center;justify-content:center;font-family:"Rye",serif;font-size:26px;letter-spacing:.55em;padding-left:.55em;color:var(--dark)}
.title--orange{background:var(--orange)}
.title--green{background:var(--green)}
.title--dark{background:var(--dark);color:var(--white)}
.title--white{background:var(--white)}
.section-body{flex:1;display:flex;flex-direction:column;justify-content:space-between;padding:6px 6px 4px;border:2px dashed;border-top:none}
.body--orange{border-color:var(--orange)}
.body--green{border-color:var(--green)}
.body--dark{border-color:var(--dark)}
.body--white{border-color:var(--white)}
.item-head{display:flex;justify-content:space-between;align-items:baseline;font-size:19px;line-height:1.1;font-weight:400}
.item-desc{font-size:10.5px;line-height:1.35;font-weight:300;color:var(--ink-soft);margin-top:2px}
.panel--middle .item-desc{color:#2b2b2b}
.item-note{font-size:11px;font-weight:400;margin-top:2px}
.photos{display:flex;gap:4px;height:68px}
.photo{flex:1;border-radius:2px}
.web{position:absolute;left:0;right:0;top:872px;text-align:center;font-size:16px;font-weight:400;color:var(--dark)}
</style>
</head>
<body>
<div class="menu">

  <div class="panel panel--left">
    <section class="section" style="top:32px;height:525px">
      <h2 class="section-title title--orange">BREAKFAST</h2>
      <div class="section-body body--orange">
        <div class="item"><div class="item-head"><span>Pastries</span><span>00</span></div><p class="item-desc">Croissant (regular, almond, chocolate)<br>Blueberry Muffin Superseed Cookie</p></div>
        <div class="item"><div class="item-head"><span>Parfait</span><span>00</span></div><p class="item-desc">Fresh strawberries and blueberries on yogurt and muesli<br>and topped with honey drizzle.</p></div>
        <div class="item"><div class="item-head"><span>Avocado Super Toast</span><span>00</span></div><p class="item-desc">Avocado Mash, Tomato, Basil, Ground Flax, Hemp Seed,<br>Chickpeas, and Moringa Powder on Whole Wheat Bread.</p></div>
        <div class="item"><div class="item-head"><span>Brunch Burger</span><span>00</span></div><p class="item-desc">House seasoned beef burger topped with an over medium egg,<br>red leaf lettuce, tomato, housemade pickles and<br>Larder Sauce on a bun.</p></div>
        <div class="item"><div class="item-head"><span>Breakfast Sammy</span><span>00</span></div><p class="item-desc">Your choice of over medium egg or tofu steak with guacamole,<br>tomato, and Larder sauce on an English muffin.</p></div>
        <div class="item"><div class="item-head"><span>AM Burrito</span><span>00</span></div><p class="item-desc">Scrambled eggs, onion, red bell pepper, black beans,<br>housemade salsa, yogurt, and pepper jack cheese in a tortilla.</p></div>
        <div class="photos">
          <div class="photo" style="background:linear-gradient(#f3e6cf,#c98a3a)" role="img" aria-label="Basket of croissants"></div>
          <div class="photo" style="background:linear-gradient(#f4f1ec,#e3d6c4)" role="img" aria-label="Yogurt parfait in a glass"></div>
          <div class="photo" style="background:linear-gradient(#e9e2d6,#8a5a32)" role="img" aria-label="Brunch burger with fried egg"></div>
          <div class="photo" style="background:linear-gradient(#c96a3c,#e8d0a8)" role="img" aria-label="Breakfast burrito on a plate"></div>
        </div>
      </div>
    </section>
    <section class="section" style="top:567px;height:301px">
      <h2 class="section-title title--green">SMOOTHIES</h2>
      <div class="section-body body--green">
        <div class="item"><div class="item-head"><span>Green Machine Smoothie</span><span>00</span></div><p class="item-desc">Romaine, spinach, banana, mango, pineapple,<br>flaxmilk, spirulina, almond butter</p></div>
        <div class="item"><div class="item-head"><span>Acai Smoothie</span><span>00</span></div><p class="item-desc">Acai, blueberries, banana, pineapple, Macqui berry,<br>flaxmilk, almond butter</p></div>
        <div class="item"><div class="item-head"><span>Mango Smoothie</span><span>00</span></div><p class="item-desc">Mango, flaxmilk, banan, hemp seeds</p></div>
        <div class="photos" style="height:76px">
          <div class="photo" style="background:linear-gradient(#eef0ea,#6a9a3a)" role="img" aria-label="Green smoothie in a glass"></div>
          <div class="photo" style="flex:2;background:linear-gradient(#f1ece8,#a8426a)" role="img" aria-label="Acai smoothie bowl with berries"></div>
          <div class="photo" style="background:linear-gradient(#f6e2a0,#e8a21c)" role="img" aria-label="Mango smoothie in a glass"></div>
        </div>
      </div>
    </section>
  </div>

  <div class="panel panel--middle">
    <section class="section" style="top:32px;height:530px">
      <h2 class="section-title title--dark">BOWLS</h2>
      <div class="section-body body--dark" style="padding-top:2px">
        <div class="item"><div class="item-head"><span>Southwest Bowl</span><span>00</span></div><p class="item-desc">Your choice of protein with corn, black beans, red onions,<br>almonds and avocado over quinoa with lime hot sauce.</p></div>
        <div class="item"><div class="item-head"><span>Chimi Bowl</span><span>00</span></div><p class="item-desc">Your choice of protein with red bell pepper, mushrooms,<br>zucchini, squash, onion, cherry tomatoes and fresh herb<br>chimichurri on wild and brown rice.</p></div>
        <div class="item"><div class="item-head"><span>Soba Noodle Bowl</span><span>00</span></div><p class="item-desc">Your choice of protein with spinach, snow peas,<br>roasted carrots, red bell pepper, cilantro, sesame seeds and<br>ginger lime sauce over soba noodles.</p></div>
        <div class="photos" style="height:60px;gap:3px">
          <div class="photo" style="background:linear-gradient(#d9c9a8,#b8402a)" role="img" aria-label="Southwest bowl with beans and corn"></div>
          <div class="photo" style="background:linear-gradient(#8a6a3a,#c24a28)" role="img" aria-label="Soba noodle bowl with vegetables"></div>
          <div class="photo" style="background:linear-gradient(#7a4a2a,#8aa84a)" role="img" aria-label="Bowl with avocado and black beans"></div>
        </div>
        <div class="item"><div class="item-head"><span>Hollywood Bowl</span><span>00</span></div><p class="item-desc">Your choice of protein with broccoli, roasted corn,<br>cherry tomatoes, basil, pepitas, flax seeds and lemon<br>juice on wild and brown rice.</p></div>
        <div class="item"><div class="item-head"><span>Larder Bowl</span><span>00</span></div><p class="item-desc">Your choice of protein with roasted chickpeas and<br>cauliflower, zesty fennel salad and citrus yogurt.</p></div>
        <div class="item"><div class="item-head"><span>Buddha Bowl</span><span>00</span></div><p class="item-desc">Your choice of protein with corn, red kale, sweet potatoes,<br>red cabbage, parsley, oregano, hummus, and farro.</p></div>
        <div class="item"><div class="item-head"><span>Chili Rice Bowl</span><span>00</span></div><p class="item-desc">Chicken, onions, bell peppers, jalapeños, black &amp;<br>kidney beans, and tomato over brown rice.</p></div>
      </div>
    </section>
    <section class="section" style="top:567px;height:295px">
      <h2 class="section-title title--white">SOUPS</h2>
      <div class="section-body body--white">
        <div class="item"><div class="item-head"><span>Chicken Noodle</span><span>00</span></div><p class="item-desc">Chicken, egg noodles, root vegetables,<br>oregano &amp; peppercorns.</p></div>
        <div class="item"><div class="item-head"><span>Larder Chili</span><span>00</span></div><p class="item-desc">Chicken, onions, bell peppers, jalapeños, black &amp;<br>kidney beans, and tomato.</p></div>
        <div class="item"><div class="item-head"><span>Seasonal Rotating</span><span>00</span></div><p class="item-note">(Butternut Squash Soup V+, GF)</p><p class="item-desc" style="margin-top:0">Butternut squash blended with warm spices, and coconut milk.</p></div>
        <div class="photos">
          <div class="photo" style="background:linear-gradient(#f3f0e8,#d9b24a)" role="img" aria-label="Bowl of vegetable soup"></div>
          <div class="photo" style="background:linear-gradient(#e6e2da,#c98a3a)" role="img" aria-label="Chicken noodle soup"></div>
          <div class="photo" style="background:linear-gradient(#f1eee8,#e39a28)" role="img" aria-label="Butternut squash soup"></div>
        </div>
      </div>
    </section>
    <p class="web">www.GrubbLarder.example</p>
  </div>

  <div class="panel panel--right">
    <section class="section" style="top:32px;height:335px">
      <h2 class="section-title title--orange">WRAPS</h2>
      <div class="section-body body--orange">
        <div class="item"><div class="item-head"><span>Rancher's Wrap</span><span>00</span></div><p class="item-desc">Tomato, red onion, hard boiled egg, avocado, feta cheese,<br>microgreens, romaine, grilled chicken and Ranch<br>dressing in a grilled wrap.</p></div>
        <div class="item"><div class="item-head"><span>Vegan Tuna Wrap</span><span>00</span></div><p class="item-desc">Vegan tuna, romaine, avocado, celery, shallot,<br>and oregano with Herbalicious Sauce in a whole grain wrap.</p></div>
        <div class="item"><div class="item-head"><span>Vegetarian Wrap</span><span>00</span></div><p class="item-desc">Roasted chickpeas, romaine, avocado, red bell pepper,<br>shaved carrots, cucumber, spinach, basil, black beans and<br>feta with lemon-hummus in a sprouted 7-grain wrap.</p></div>
        <div class="photos" style="height:72px">
          <div class="photo" style="background:linear-gradient(#e8e2d0,#8aa84a)" role="img" aria-label="Sliced vegetable wraps"></div>
          <div class="photo" style="flex:.8;background:linear-gradient(#2a3a4a,#c9a15a)" role="img" aria-label="Halved wrap with filling"></div>
          <div class="photo" style="background:linear-gradient(#f0f0ec,#6a8a3a)" role="img" aria-label="Spinach wraps on a plate"></div>
        </div>
      </div>
    </section>
    <section class="section" style="top:378px;height:492px">
      <h2 class="section-title title--dark">SALAD</h2>
      <div class="section-body body--dark">
        <div class="item"><div class="item-head"><span>Avocado, Golden Beet,<br>and Cranberry Salad</span><span>00</span></div><p class="item-desc">Gold beets, avocado, dried cranberries, watermelon radish,<br>red kale, romaine, mixed greens, and pepitas served with<br>Golden Buddha dressing.</p></div>
        <div class="item"><div class="item-head"><span>Burrata Salad</span><span>00</span></div><p class="item-desc">Tomato, melon, shredded basil, balsamic glaze,<br>fresh cracked pepper, and olive oil with burrata.</p></div>
        <div class="item"><div class="item-head"><span>Mediterranean Salad</span><span>00</span></div><p class="item-desc">Cucumbers, Kalamata olives, cherry tomatoes, parsley,<br>tricolor quinoa, hard-boiled egg, and hummus on mixed greens,<br>romaine, and red cabbage with lemon-olive oil dressing.</p></div>
        <div class="item"><div class="item-head"><span>Vegan Chef Salad</span><span>00</span></div><p class="item-desc">Roasted potatoes and carrots, chickpeas, avocado,<br>microgreens and walnuts on mixed greens, romaine,<br>and red kale with vegan ranch.</p></div>
        <div class="item"><div class="item-head"><span>Rancher's Salad</span><span>00</span></div><p class="item-desc">Tomato, red onion, hard boiled egg, avocado, feta cheese,<br>microgreens, and grilled chicken on romaine with Ranch dressing.</p></div>
        <div class="photos">
          <div class="photo" style="background:linear-gradient(#e9dcc0,#c0402a)" role="img" aria-label="Chef salad with egg and greens"></div>
          <div class="photo" style="background:linear-gradient(#f0ece4,#d6502a)" role="img" aria-label="Tomato and burrata salad"></div>
          <div class="photo" style="flex:1.3;background:linear-gradient(#d8d8d8,#3a5a2a)" role="img" aria-label="Kale salad with pomegranate"></div>
        </div>
      </div>
    </section>
  </div>

</div>
</body>
</html>
```